Firm Stationery Design

I need a design for stationery, including: Stationery First Page, Stationery Second Sheet, Envelope, Mailing Label for Flat Envelopes, and Business Cards

```html
<!DOCTYPE html>
<html lang="en">
<head>
<meta charset="utf-8">
<title>Harlow Law LLC – Business Cards</title>
<link rel="stylesheet" href="https://fonts.googleapis.com/css2?family=Archivo+Black&display=swap">
<style>
  :root {
    --backdrop: #e0e0e0;
    --paper: #ffffff;
    --ink: #000000;
    --charcoal: #18191b;
    --amber: #ffa000;
    --rule: #f0ece4;
  }
  html, body {
    margin: 0;
    padding: 0;
    width: 976px;
    height: 1200px;
    overflow: hidden;
    background: var(--backdrop);
  }
  .sheet {
    display: block;
    width: 976px;
    height: 1200px;
  }
  .firm-name {
    font-family: "Archivo Black", sans-serif;
  }
  .card-paper { fill: var(--paper); }
  .card-dark { fill: var(--charcoal); }
  .band-ink { fill: var(--ink); }
  .band-paper { fill: var(--paper); }
  .mark-square { fill: var(--amber); }
  .name-ink { fill: var(--ink); }
  .name-amber { fill: var(--amber); }
  .contact-rule { stroke: var(--rule); stroke-width: 6; }
  .contact-icon { fill: var(--paper); }
  .icon-line { fill: none; stroke: var(--charcoal); }
</style>
</head>
<body>
<svg class="sheet" viewBox="0 0 1500 1844" xmlns="http://www.w3.org/2000/svg" aria-label="Harlow Law LLC business card, front and back">

  <!-- Card front -->
  <g class="card card-front">
    <rect class="card-paper" x="45" y="38" width="1421" height="850"/>
    <path class="band-ink" d="M45,560 C400,580 700,520 900,465 C1150,405 1350,405 1466,425 L1466,455 C1350,438 1150,440 900,495 C700,545 400,600 45,578 Z"/>
    <path class="card-dark" d="M45,595 C400,615 700,560 900,515 C1150,460 1350,460 1466,480 L1466,888 L45,888 Z"/>

    <rect class="mark-square" x="215" y="93" width="180" height="180"/>
    <text class="firm-name name-ink" x="140" y="378" font-size="80" textLength="338" lengthAdjust="spacingAndGlyphs">HARLOW</text>
    <text class="firm-name name-amber" x="172" y="441" font-size="36" textLength="275" lengthAdjust="spacing">LAW LLC</text>

    <g class="contact-list">
      <path class="contact-icon" d="M136,622 l8,-3 l6,11 l-5,4 c3,6 7,10 12,12 l4,-5 l11,6 l-2,8 c-18,2 -36,-15 -34,-33 Z"/>
      <line class="contact-rule" x1="225" y1="660" x2="1105" y2="660"/>

      <rect class="contact-icon" x="132" y="700" width="40" height="27"/>
      <path class="icon-line" d="M132,700 L152,716 L172,700 M132,727 L147,713 M172,727 L157,713" stroke-width="2"/>
      <line class="contact-rule" x1="225" y1="731" x2="1105" y2="731"/>

      <circle class="contact-icon" cx="152" cy="797" r="31"/>
      <rect class="icon-line" x="135" y="785" width="34" height="24" stroke-width="3"/>
      <path class="icon-line" d="M135,785 L152,799 L169,785" stroke-width="3"/>
      <line class="contact-rule" x1="225" y1="802" x2="1105" y2="802"/>
    </g>
  </g>

  <!-- Card back -->
  <g class="card card-back">
    <rect class="card-dark" x="45" y="961" width="1421" height="850"/>
    <rect class="mark-square" x="622" y="1078" width="252" height="252"/>
    <text class="firm-name name-amber" x="755" y="1480" font-size="110" text-anchor="middle" textLength="478" lengthAdjust="spacingAndGlyphs">HARLOW</text>
    <text class="firm-name name-amber" x="755" y="1570" font-size="54" text-anchor="middle" textLength="390" lengthAdjust="spacing">LAW LLC</text>

    <path class="band-paper" d="M45,1700 C500,1640 1000,1700 1466,1690 L1466,1730 C1000,1745 500,1690 45,1745 Z"/>
  </g>
</svg>
</body>
</html>
```